2021 IT Training Presentation Deck Refresh

Copper Lantern is an IT education services firm. We teach IT industry standards and technologies. We are in need of an updated training presentation deck that factors in a fresh take for:

1) Agenda/Table of Contents
2) Chapter Topic Summary
2) Chapter Introduction and Learning Objectives
3) Chapter Recaps
4) Important Point/Pro Tip emphasis
5) Warning Message
6) Mini Quiz layout
7) Lab Exercise Introduction
7) Deck Close Out

Incorporating the official Copper Lantern colour palette for materials that will likely be used in self-paced/online recorded versions of courses.

Target Market(s)

IT

Industry/Entity Type

Computer Training

Requirements
Nice to have
• placeholder sections for images of IT workers in an office or by a computer

```html
<!DOCTYPE html>
<html lang="en">
<head>
<meta charset="utf-8">
<title>Copper Lantern – Training Deck Overview</title>
<link href="https://fonts.googleapis.com/css2?family=Lato:wght@300;400;700&display=swap" rel="stylesheet">
<style>
:root{
  --board-grey:#8b8b8b;
  --band-blue:#6499d4;
  --deep-navy:#1c1b4b;
  --navy:#1e1d5b;
  --mid-blue:#354f98;
  --sky:#6aa5dc;
  --accent:#2f5ea8;
  --ice:#d6eef5;
  --ink:#1b1b2e;
  --body:#3b4a5c;
  --teal:#2aa3c4;
  --sun:#fbef4a;
  --ocean:#1a5fa0;
}
*{box-sizing:border-box;margin:0;padding:0}
html,body{width:973px;height:1200px;overflow:hidden;background:var(--board-grey)}
body{position:relative;font-family:'Lato',sans-serif;color:var(--ink)}
.board-bg{position:absolute;inset:0}
.slide{position:absolute;width:446px;height:208px;background:var(--ice);overflow:hidden;box-shadow:0 4px 10px rgba(0,0,0,.35)}
.col-left{left:31px}.col-right{left:496px}
.row-1{top:39px}.row-2{top:267px}.row-3{top:496px}.row-4{top:725px}.row-5{top:953px}
.layer{position:absolute;inset:0}
.brand-tag{position:absolute;right:13px;font-size:7px;letter-spacing:.2px;color:var(--accent);font-weight:400;white-space:nowrap}
.slide-title{position:absolute;font-weight:400;font-size:15px;letter-spacing:.2px;color:var(--ink);line-height:1.2;white-space:nowrap}
.slide-title .hl{color:var(--accent)}
.copy{position:absolute;font-size:6px;line-height:11.3px;color:var(--body)}
.cover-badge{position:absolute;border-radius:50%;background:#fff;border:3px solid var(--navy);box-shadow:0 0 0 2px #fff;display:flex;align-items:center;justify-content:center;text-align:center}
.cover-badge span{color:var(--mid-blue);font-weight:300;line-height:1.05;letter-spacing:.5px}
/* table of contents */
.toc-row{position:absolute;left:12px;top:60px;width:422px;height:116px;display:flex;gap:3.4px}
.toc-card{flex:1;min-width:0;color:#fff;padding:18px 3px 0;text-align:center}
.toc-card h3{font-size:6.4px;font-weight:700;line-height:8.8px;margin-bottom:6px;white-space:nowrap}
.toc-card p{font-size:4.6px;line-height:8px;font-weight:400;opacity:.95;padding:0 2px}
.toc-mid{background:var(--mid-blue)}.toc-navy{background:var(--navy)}.toc-sky{background:var(--sky)}
/* quiz */
.quiz-pill{position:absolute;height:22px;width:208px;background:#fff;border-radius:11px;display:flex;align-items:center;padding-left:17px;font-size:7.6px;font-weight:700;color:var(--ink);white-space:nowrap}
.quiz-pill .toggle{position:absolute;right:4px;top:3px;width:16px;height:16px;border-radius:50%;background:var(--mid-blue);color:#fff;font-size:12px;line-height:15px;text-align:center;font-weight:700}
.q-left{left:11px}.q-right{left:227px}
.about-name{position:absolute;left:13px;top:46px;font-size:21px;font-weight:300;color:var(--accent);letter-spacing:.5px;white-space:nowrap}
.mark-word{position:absolute;font-weight:300;color:var(--navy);letter-spacing:1px;text-align:center;white-space:nowrap}
</style>
</head>
<body>

<svg class="board-bg" width="973" height="1200" viewBox="0 0 973 1200" aria-hidden="true">
  <rect width="973" height="1200" fill="var(--board-grey)"/>
  <path d="M0 0H973V44C700 38 520 60 470 75C380 90 200 50 0 30Z" fill="var(--band-blue)"/>
  <path d="M0 1095C250 1060 420 1045 560 1050C720 1055 860 1075 973 1095V1200H0Z" fill="var(--deep-navy)"/>
</svg>

<!-- Cover -->
<section class="slide col-left row-1" style="background:var(--navy)">
  <div class="layer" role="img" aria-label="Photo of an IT worker typing at a laptop in a dim office, tinted blue" style="background:linear-gradient(120deg,#141a52 0%,#25347d 45%,#1a2160 100%)"></div>
  <svg class="layer" width="446" height="208" aria-hidden="true">
    <polygon points="170,0 250,0 330,105 250,208 170,208 250,105" fill="#2d4aa0" opacity=".55"/>
    <polygon points="250,0 330,0 390,105 330,208 250,208 330,105" fill="#6aa5dc" opacity=".45"/>
    <rect x="0" y="168" width="135" height="40" fill="#5b8ec8" opacity=".55"/>
  </svg>
  <div class="cover-badge" style="left:53px;top:25px;width:117px;height:117px"><span style="font-size:13px">COPPER<br>LANTERN</span></div>
</section>

<!-- Pro tip -->
<section class="slide col-right row-1">
  <svg class="layer" width="446" height="208" aria-hidden="true">
    <circle cx="106" cy="106" r="86" fill="none" stroke="#3aa7d8" stroke-width="1"/>
    <circle cx="106" cy="106" r="82" fill="#fff"/>
    <path d="M106 106 L106 28 A78 78 0 0 1 173.5 145 Z" fill="var(--sun)"/>
    <path d="M106 106 L173.5 145 A78 78 0 0 1 38.5 145 Z" fill="var(--ocean)"/>
    <path d="M106 106 L38.5 145 A78 78 0 0 1 106 28 Z" fill="var(--teal)"/>
    <line x1="106" y1="106" x2="106" y2="28" stroke="#fff" stroke-width="3"/>
    <line x1="106" y1="106" x2="173.5" y2="145" stroke="#fff" stroke-width="3"/>
    <line x1="106" y1="106" x2="38.5" y2="145" stroke="#fff" stroke-width="3"/>
    <path d="M103 14 l4 -2 l-4 -2" fill="none" stroke="#3aa7d8" stroke-width="1"/>
    <circle cx="80" cy="62" r="6" fill="none" stroke="#fff" stroke-width="1"/>
    <circle cx="137" cy="64" r="7" fill="none" stroke="#1b1b2e" stroke-width="1"/>
    <circle cx="137" cy="64" r="3.5" fill="none" stroke="#1b1b2e" stroke-width="1"/>
    <text font-family="Lato,sans-serif" font-size="4" fill="#fff"><tspan x="52" y="80">Lorem ipsum dolor</tspan><tspan x="52" y="85">sit amet, consectetur</tspan><tspan x="52" y="90">adipiscing elit, sed</tspan><tspan x="52" y="95">do eiusmod tempor</tspan><tspan x="52" y="100">et dolore magna.</tspan></text>
    <text font-family="Lato,sans-serif" font-size="4" fill="#1b1b2e"><tspan x="129" y="80">Lorem ipsum dolor</tspan><tspan x="129" y="85">sit amet, consectetur</tspan><tspan x="129" y="90">adipiscing elit, sed</tspan><tspan x="129" y="95">do eiusmod tempor</tspan><tspan x="129" y="100">et dolore magna.</tspan></text>
    <text font-family="Lato,sans-serif" font-size="4" fill="#fff"><tspan x="79" y="150">Lorem ipsum dolor sit amet,</tspan><tspan x="79" y="155">consectetur adipiscing elit</tspan><tspan x="79" y="160">do eiusmod tempor incidunt</tspan><tspan x="79" y="165">ut labore et dolore magna.</tspan></text>
  </svg>
  <span class="brand-tag" style="top:36px">COPPER LANTERN</span>
  <h2 class="slide-title" style="left:222px;top:38px">PRO TIP <span class="hl">EMPHASIS</span></h2>
  <p class="copy" style="left:223px;top:68px;width:172px">Lorem ipsum dolor sit amet, consectetur adipiscing elit, sed do eiusmod tempor incididunt ut labore et dolore magna aliquis ipsum suspendisse ultrices gravida. Risus commodo viverra maecenas accumsan lacus vel facilisis. Lorem ipsum dolor sit amet, consectetur adipiscing elit, sed do ei tempor incididunt ut labore et dolore magna aliquis ipsum suspendisse ultrices gravidus commoa maecenas accupiscing elit, sed do ei tempor incididunt ut labore et dolore magna aliquis ipsum suspendisse ultrices gravidus commoa maecenas msan lacilisis.</p>
</section>

<!-- Table of contents -->
<section class="slide col-left row-2">
  <span class="brand-tag" style="top:34px">COPPER LANTERN</span>
  <h2 class="slide-title" style="left:13px;top:20px">TABLE OF <span class="hl">CONTENTS</span></h2>
  <div class="toc-row">
    <div class="toc-card toc-mid"><h3>TOPIC SUMMARY</h3><p>Lorem ipsum dolor sit amet, consectetur adipiscing elit, sed do eiusmod tempor incididunt ut labore et doloregnaquauis ipsum suspendisse ultrices gravidisus commodo viverra maecenas accumsan lacus vel facilisis.</p></div>
    <div class="toc-card toc-navy"><h3>CHAPTER<br>INTRODUCTION AND<br>LEARNING OBJECTIVES</h3><p>Lorem ipsum dolor sit amet, consectetur adipiscing elit, sed do eiusmod tempor incididunt ut labore et doloregnaquauis ipsum suspendisse ultrices gravidisus commodo viverra</p></div>
    <div class="toc-card toc-mid"><h3>CHAPTER RECAPS</h3><p>Lorem ipsum dolor sit amet, consectetur adipiscing elit, sed do eiusmod tempor incididunt ut labore et doloregnaquauis ipsum suspendisse ultrices gravidisus commodo viverra maecenas accumsan lacus vel facilisis.</p></div>
    <div class="toc-card toc-sky"><h3>PRO TIP EMPHASIS</h3><p>Lorem ipsum dolor sit amet, consectetur adipiscing elit, sed do eiusmod tempor incididunt ut labore et doloregnaquauis ipsum suspendisse ultrices gravidisus commodo viverra maecenas accumsan lacus vel facilisis.</p></div>
    <div class="toc-card toc-navy"><h3>LAB EXERCISE</h3><p>Lorem ipsum dolor sit amet, consectetur adipiscing elit, sed do eiusmod tempor incididunt ut labore et doloregnaquauis ipsum suspendisse ultrices gravidisus commodo viverra maecenas accumsan lacus vel facilisis.</p></div>
  </div>
</section>

<!-- Warning -->
<section class="slide col-right row-2">
  <svg class="layer" width="446" height="208" aria-hidden="true">
    <polygon points="260,78 320,0 345,0 272,82" fill="var(--navy)"/>
    <polygon points="305,40 370,0 446,0 446,5" fill="var(--sky)"/>
    <polygon points="185,208 232,140 240,170 205,208" fill="var(--navy)"/>
    <polygon points="205,208 240,170 244,208" fill="var(--sky)"/>
  </svg>
  <div class="layer" role="img" aria-label="Photo of a red and yellow warning triangle with caution tape on a concrete wall" style="clip-path:polygon(230px 94px,446px 2px,446px 208px,244px 208px);background:radial-gradient(circle at 62% 58%,#f2b21c 0%,#d8341e 22%,#5d5b58 45%,#3a3937 100%)"></div>
  <span class="brand-tag" style="left:221px;right:auto;top:31px">COPPER LANTERN</span>
  <h2 class="slide-title" style="left:21px;top:31px">WARNING <span class="hl">MESSAGE</span></h2>
  <p class="copy" style="left:21px;top:60px;width:170px">Lorem ipsum dolor sit amet, consectetur adipiscing elit, sed do eiusmod tempor incididunt ut labore et dolore magna aliquis ipsum suspendisse ultrices gravida. Risus commodo viverra maecenas accumsan lacus vel facilisis. Lorem ipsum dolor sit amet, consectetur adipiscing elit, sed do ei tempor incididunt ut labore et dolore magna aliquis ipsum suspendisse ultrices gravidus commoa maecenas accupiscing elit,Lorem ipsum dolor sit amet, consectetur adipiscing elit, sed do eiusmod tempor incididunt ut labore et dolore magna aliquiuspendisse ultrices gravida commodo viverra maecenas</p>
</section>

<!-- About -->
<section class="slide col-left row-3">
  <span class="brand-tag" style="top:35px">COPPER LANTERN</span>
  <h2 class="slide-title" style="left:14px;top:21px">ABOUT</h2>
  <h1 class="about-name">COPPER LANTERN</h1>
  <p class="copy" style="left:14px;top:86px;width:172px">Lorem ipsum dolor sit amet, consectetur adipiscing elit, sed do eiusmod tempor incididunt ut labore et dolore magna aliquis ipsum suspendisse ultrices gravida. Risus commodo viverra maecenas accumsan lacus vel facilisis. Lorem ipsum dolor sit amet, consectetur adipiscing elit, sed do ei tempor incididunt ut labore et dolore magna aliquis ipsum suspendisse ultrices gravidus commoa maecenas accupiscing elit, sed do ei tempor incididunt ut labore et dolore magna aliquis ipsum suspendisse ultrices gravidus commoa maecenas msan lacilisis.</p>
  <div class="mark-word" style="left:215px;top:90px;width:220px;font-size:20px">COPPER LANTERN</div>
</section>

<!-- Mini quiz -->
<section class="slide col-right row-3">
  <span class="brand-tag" style="top:30px">COPPER LANTERN</span>
  <h2 class="slide-title" style="left:17px;top:16px">MINI <span class="hl">QUIZ</span></h2>
  <div class="quiz-pill q-left" style="top:56px">Sed ut perspiciatis unde omnis iste natus?<span class="toggle">+</span></div>
  <div class="quiz-pill q-right" style="top:56px">Lorem ipsum dolor sit amet, consectetur?<span class="toggle">+</span></div>
  <div class="quiz-pill q-left" style="top:87px">Duis aute irure dolor in reprehenderits?<span class="toggle">+</span></div>
  <div class="quiz-pill q-right" style="top:87px">Sed ut perspiciatis unde omnis iste natus?<span class="toggle">+</span></div>
  <div class="quiz-pill q-left" style="top:119px">Excepteur sint occaecat cupnt ioidensunt i?<span class="toggle">−</span></div>
  <div class="quiz-pill q-right" style="top:119px">Quis autem vel eum iure reprehenderis?<span class="toggle">+</span></div>
  <p class="copy" style="left:11px;top:154px;width:426px">Lorem ipsum dolor sit amet, consectetur adipiscing elit, sed do eiusmod tempor incididunt ut labore et dolore magna aliquis ipsum suspendisse ultriravida. Risus commodo viverra maecenas accumsan lacus vel facilisis. Lorem ipsum dolor sit amet, consectetur adipiscing elit, sed do ei tempor incididunt ut labore et dolore magna aliquis ipsum suspendisse ultrices gravidus commoa maecenas accupiscing elit,Lorem ipsum dolor sit amet,</p>
</section>

<!-- Chapter intro -->
<section class="slide col-left row-4">
  <svg class="layer" width="446" height="208" aria-hidden="true">
    <polygon points="10,0 145,0 188,75" fill="var(--sky)"/>
    <polygon points="145,0 165,0 262,208 242,208 210,140" fill="var(--navy)"/>
    <polygon points="208,150 242,208 205,208" fill="var(--sky)"/>
  </svg>
  <div class="layer" role="img" aria-label="Photo of a laptop showing a video call with many participants" style="clip-path:polygon(0 8px,122px 42px,218px 86px,210px 208px,0 208px);background:linear-gradient(135deg,#4a4036 0%,#8a7560 40%,#c9b9a4 70%,#6e5a45 100%)"></div>
  <span class="brand-tag" style="top:37px">COPPER LANTERN</span>
  <h2 class="slide-title" style="left:258px;top:32px;line-height:20px">CHAPTER<br><span class="hl">INTRODUCTION AND</span><br>LEARNING OBJECTIVES</h2>
  <p class="copy" style="left:259px;top:97px;width:172px">Lorem ipsum dolor sit amet, consectetur adipiscing elit, sed do eiusmod tempor incididunt ut labore et dolore magna aliquis ipsum suspendisse ultrices gravida. Risus commodo viverra maecenas accumsan lacus vel facilisis. Lorem ipsum dolor sit amet, consectetur adipiscing elit, sed do ei tempor incididunt ut labore et dolore magna aliquis ipsum suspendisse ultrices gravidus commoa maecenas accupiscing elit,</p>
</section>

<!-- Lab exercise -->
<section class="slide col-right row-4">
  <div class="layer" role="img" aria-label="Photo of a bright office with a person typing on a laptop, tinted grey blue" style="background:linear-gradient(100deg,#9fb0bf 0%,#b9c6d0 50%,#c7cfd6 100%)"></div>
  <svg class="layer" width="446" height="208" aria-hidden="true">
    <polygon points="150,0 270,0 360,108 270,208 150,208 240,108" fill="#4a5c86" opacity=".55"/>
    <polygon points="185,0 250,0 360,108 250,208 185,208 300,108" fill="var(--navy)" opacity=".9"/>
    <rect x="0" y="168" width="150" height="40" fill="#5b8ec8" opacity=".6"/>
    <polygon points="0,0 150,0 240,108 0,168" fill="#d6eef5" opacity=".35"/>
  </svg>
  <span class="brand-tag" style="top:30px">COPPER LANTERN</span>
  <h2 class="slide-title" style="left:20px;top:27px">LAB <span class="hl">EXERCISE</span></h2>
  <p class="copy" style="left:21px;top:56px;width:165px">Lorem ipsum dolor sit amet, consectetur adipiscing elit, sed do eiusmod tempor incididunt ut labore et dolore magna aliquis ipsum suspendisse ultriravida. Risus commodo viverra maecenas accumsan lacus vel facilisorem ipsum dolor sit amet, consectetur adipiscing elit, sed do ei tempor incididunt ut labore et dolore mag suspendisse ultrices gravidus commoa maecenas accupiscing elit,</p>
</section>

<!-- Close out -->
<section class="slide col-left row-5" style="background:linear-gradient(160deg,#31268a 0%,#3a3da6 50%,#5069d0 100%)">
  <div class="cover-badge" style="left:148px;top:29px;width:151px;height:151px;border-color:var(--mid-blue)"><span style="font-size:17px">COPPER<br>LANTERN</span></div>
</section>

</body>
</html>
```